Logo and label lay out for Copper Thistle wines

Wine Bottle label for single vineyard on The Mornington Peninsula, Victoria, Australia
Name of Vineyard is “Copper Thistle”
(A copper Thistle is a common biting ant found in the vineyard.)
The name and vintage of each of the four varieties of wine will need to be included on the label.
We want an instantly recognisable image on the label along with the name Copper Thistle.

Target Market(s)

Quality wine for cafes, restaurants and individual’s wine collection

Industry/Entity Type

Vineyard

Logo Text

Copper Thistle

Logo styles of interest
Emblem Logo
Abstract Logo
Colors

Designer to choose colors to be used in the design.

Requirements
Must have
• Simple yet stylish image, instantly recognisable .
Nice to have
• Possibly a stylistic image of an ant
Should not have
• Not an overly detailed image.

```html
<!DOCTYPE html>
<html lang="en">
<head>
<meta charset="utf-8">
<title>Copper Thistle – Logo and Label Layout</title>
<link rel="stylesheet" href="https://fonts.googleapis.com/css2?family=Open+Sans:wght@400&display=swap">
<style>
  :root {
    --ink: #000000;
    --paper: #ffffff;
    --pinot-gris: #f4a81d;
    --shiraz: #d71f2b;
    --merlot: #2b3284;
    --cabernet: #a0197f;
  }
  html, body {
    margin: 0;
    padding: 0;
    overflow: hidden;
  }
  body {
    width: 1200px;
    height: 1000px;
    background: var(--paper);
    position: relative;
    font-family: "Open Sans", Arial, sans-serif;
    color: var(--ink);
  }

  /* Primary brand lockup */
  .brand-mark {
    position: absolute;
    left: 213px;
    top: 370px;
    width: 60px;
    height: 60px;
    border-radius: 50%;
    background: var(--ink);
  }
  .brand-lockup {
    position: absolute;
    left: 95px;
    top: 524px;
    width: 300px;
    margin: 0;
    text-align: center;
    font-size: 50px;
    font-weight: 400;
    line-height: 56px;
    letter-spacing: 1px;
  }

  /* Wine labels */
  .label {
    position: absolute;
    width: 252px;
    height: 317px;
    border: 2px solid var(--ink);
    background: var(--paper);
    overflow: hidden;
  }
  .label--pinot-gris { left: 524px; top: 137px; --accent: var(--pinot-gris); }
  .label--shiraz     { left: 824px; top: 137px; --accent: var(--shiraz); }
  .label--merlot     { left: 524px; top: 542px; --accent: var(--merlot); }
  .label--cabernet   { left: 824px; top: 542px; --accent: var(--cabernet); }

  .label__band {
    position: absolute;
    top: 0;
    width: 65px;
    height: 317px;
    background: var(--accent);
  }
  .label__band::after {
    content: "";
    position: absolute;
    top: 6px;
    bottom: 6px;
    background: var(--ink);
  }
  .label__band--left { left: 0; }
  .label__band--left::after { left: 6px; right: 0; }
  .label__band--right { right: 0; width: 64px; }
  .label__band--right::after { left: 0; right: 6px; }

  .label__mark {
    position: absolute;
    left: 111px;
    top: 44px;
    width: 30px;
    height: 30px;
    border-radius: 50%;
    background: var(--ink);
  }
  .label__name {
    position: absolute;
    left: 65px;
    width: 122px;
    top: 110px;
    margin: 0;
    text-align: center;
    font-size: 19px;
    font-weight: 400;
    line-height: 22px;
    letter-spacing: 0.5px;
  }
  .label__trail {
    position: absolute;
    left: 6px;
    top: 152px;
    width: 256px;
    height: 12px;
    transform-origin: 0 50%;
    transform: rotate(20.5deg);
    background: linear-gradient(90deg, var(--paper) 0%, var(--accent) 35%, var(--accent) 65%, var(--paper) 100%);
    border-radius: 6px;
  }
  .label__variety {
    position: absolute;
    left: 65px;
    width: 122px;
    top: 264px;
    margin: 0;
    text-align: center;
    font-size: 11px;
    line-height: 14px;
  }
  .label__vintage {
    position: absolute;
    left: 65px;
    width: 122px;
    top: 280px;
    margin: 0;
    text-align: center;
    font-size: 9px;
    line-height: 12px;
  }
</style>
</head>
<body>
  <div class="brand-mark" aria-hidden="true"></div>
  <h1 class="brand-lockup">COPPER<br>THISTLE</h1>

  <section class="label label--pinot-gris">
    <div class="label__band label__band--left"></div>
    <div class="label__band label__band--right"></div>
    <div class="label__mark" aria-hidden="true"></div>
    <h2 class="label__name">COPPER<br>THISTLE</h2>
    <div class="label__trail" role="img" aria-label="Stylised trail of ants marching across the label"></div>
    <p class="label__variety">Pinot Gris</p>
    <p class="label__vintage">2019</p>
  </section>

  <section class="label label--shiraz">
    <div class="label__band label__band--left"></div>
    <div class="label__band label__band--right"></div>
    <div class="label__mark" aria-hidden="true"></div>
    <h2 class="label__name">COPPER<br>THISTLE</h2>
    <div class="label__trail" role="img" aria-label="Stylised trail of ants marching across the label"></div>
    <p class="label__variety">Shiraz</p>
    <p class="label__vintage">2019</p>
  </section>

  <section class="label label--merlot">
    <div class="label__band label__band--left"></div>
    <div class="label__band label__band--right"></div>
    <div class="label__mark" aria-hidden="true"></div>
    <h2 class="label__name">COPPER<br>THISTLE</h2>
    <div class="label__trail" role="img" aria-label="Stylised trail of ants marching across the label"></div>
    <p class="label__variety">Merlot</p>
    <p class="label__vintage">2019</p>
  </section>

  <section class="label label--cabernet">
    <div class="label__band label__band--left"></div>
    <div class="label__band label__band--right"></div>
    <div class="label__mark" aria-hidden="true"></div>
    <h2 class="label__name">COPPER<br>THISTLE</h2>
    <div class="label__trail" role="img" aria-label="Stylised trail of ants marching across the label"></div>
    <p class="label__variety">Cabernet</p>
    <p class="label__vintage">2019</p>
  </section>
</body>
</html>
```